Wine Bottle Label Graphic Design (mini bottle 187ml)

Looking for a contemporary custom wine label design for party favors. Inspiration photos provided. **Please see "wine favorite" example in uploads.

Artwork 2.5" wide by 2.75" tall to be placed on 3"x3" stickers. Specs from printer attached but I still want image to fit within the artwork size I specified. Please make label center justified. This is for BOYS. It does not need to be super "masculine"...but definitely not feminine.

Required elements:

Colors: white background, include gold and purple to match logo. Other colors are fine to include.

Name: Sababa 13 (I like use of the No) as shown in the sample, but not required
Varietal: Mitzvah Blend 6.11.2021
Vineyard: Hollis Family Vineyard
Location: Maryland
Logo: See attached (KRNotecard Final)

Font styles to use
Serif
Sans Serif

Requirements
Must have
• All the above elements. Clean and crisp design. Contemporary and classy. Purple, Gold, Black colors. See logo. You CAN include cursive font for select elements. I don't mind a combination of print and script.
Should not have
• Floral, scrolling, background image, old fashioned

```html
<!DOCTYPE html>
<html lang="en">
<head>
<meta charset="utf-8">
<title>Sababa 13 — Mitzvah Blend Label</title>
<link rel="stylesheet" href="https://fonts.googleapis.com/css2?family=Libre+Baskerville:wght@400;700&family=Pinyon+Script&family=Playfair+Display:ital,wght@1,700&family=Oswald:wght@300&display=swap">
<style>
  :root {
    --backdrop: #3b3d42;
    --label-white: #ffffff;
    --gold: #c9a343;
    --purple: #4a2f8c;
    --ink: #1d1d1f;
  }
  html, body {
    margin: 0;
    width: 1200px;
    height: 1200px;
    overflow: hidden;
    background: var(--backdrop);
  }
  .canvas {
    position: relative;
    width: 1200px;
    height: 1200px;
  }
  .label {
    position: absolute;
    left: 220px;
    top: 180px;
    width: 760px;
    height: 825px;
  }
  .label-shape {
    position: absolute;
    inset: 0;
  }
  .label-text {
    position: absolute;
    left: 0;
    width: 760px;
    text-align: center;
    margin: 0;
  }
  .brand-name {
    top: 74px;
    font-family: "Libre Baskerville", serif;
    font-weight: 700;
    font-size: 22px;
    line-height: 34px;
    letter-spacing: 2px;
    color: var(--purple);
  }
  .vineyard {
    top: 280px;
    font-family: "Libre Baskerville", serif;
    font-size: 17px;
    letter-spacing: 0.5px;
    color: var(--ink);
  }
  .wine-name {
    top: 312px;
    font-family: "Pinyon Script", cursive;
    font-weight: 400;
    font-size: 104px;
    line-height: 1;
    color: var(--purple);
  }
  .wine-number {
    top: 426px;
    font-family: "Playfair Display", serif;
    font-style: italic;
    font-weight: 700;
    font-size: 112px;
    line-height: 1;
    color: var(--purple);
  }
  .varietal {
    top: 588px;
    font-family: "Oswald", sans-serif;
    font-weight: 300;
    font-size: 26px;
    letter-spacing: 2px;
    color: var(--ink);
  }
  .vintage {
    top: 622px;
    font-family: "Oswald", sans-serif;
    font-weight: 300;
    font-size: 22px;
    letter-spacing: 12px;
    color: var(--ink);
  }
  .origin-lead {
    top: 688px;
    left: -70px;
    font-family: "Oswald", sans-serif;
    font-weight: 300;
    font-size: 16px;
    color: var(--ink);
  }
  .origin {
    top: 716px;
    font-family: "Pinyon Script", cursive;
    font-size: 64px;
    line-height: 1;
    color: var(--ink);
  }
</style>
</head>
<body>
<main class="canvas">
  <section class="label">
    <svg class="label-shape" width="760" height="825" viewBox="0 0 760 825" aria-hidden="true">
      <path d="M0,345 C0,235 130,150 290,175 A110,110 0 1 1 470,175 C630,150 760,235 760,345 L760,790 A35,35 0 0 0 725,825 L35,825 A35,35 0 0 0 0,790 Z" fill="var(--label-white)"/>
      <path d="M16,345 C16,245 140,160 318,185 A96,96 0 1 1 442,185 C620,160 744,245 744,345 L744,782 A30,30 0 0 0 714,809 L46,809 A30,30 0 0 0 16,782 Z" fill="none" stroke="var(--gold)" stroke-width="3"/>
      <line x1="246" y1="450" x2="246" y2="520" stroke="var(--gold)" stroke-width="1.5"/>
      <line x1="514" y1="450" x2="514" y2="520" stroke="var(--gold)" stroke-width="1.5"/>
      <line x1="240" y1="560" x2="520" y2="560" stroke="var(--gold)" stroke-width="2.5"/>
    </svg>

    <p class="label-text brand-name">KAI AND<br>REUBEN</p>
    <p class="label-text vineyard">HOLLIS FAMILY VINEYARD</p>
    <h1 class="label-text wine-name">Sababa</h1>
    <p class="label-text wine-number">13</p>
    <p class="label-text varietal">MITZVAH BLEND</p>
    <p class="label-text vintage">2·0·2·1</p>
    <p class="label-text origin-lead">Made In</p>
    <p class="label-text origin">Maryland</p>
  </section>
</main>
</body>
</html>
```